Dog Grass Website

We need a two page website for our new product that will be shipped to customers of a tray with grass inside for a pet to relieve themselves. We are hoping for a clean look that translates a positive and upscale message.

The first page will be informative about the product and the second page will be 'about us'.

For more information please download the files. We have attached a screenshot of what the product box will look like

Gathering more feedback

```html
<!DOCTYPE html>
<html lang="en">
<head>
<meta charset="utf-8">
<title>PawPatch Grass</title>
<link href="https://fonts.googleapis.com/css2?family=Archivo:wght@400;500;600;700;800&display=swap" rel="stylesheet">
<style>
  :root {
    --blush: #fdeeed;
    --green: #6cc24a;
    --brown: #5a1f0e;
    --white: #ffffff;
    --ink: #111111;
  }
  * { margin: 0; padding: 0; box-sizing: border-box; }
  html, body { width: 1200px; height: 675px; overflow: hidden; background: var(--white); }
  body { font-family: "Archivo", Arial, sans-serif; color: var(--brown); position: relative; }

  .hero { position: absolute; left: 0; top: 0; width: 1200px; height: 561px; background: var(--blush); }
  .hero-photo {
    position: absolute; left: 415px; top: 0; width: 785px; height: 561px;
    background: linear-gradient(120deg, #e6e4e6 0%, #cfc8c9 35%, #8a7570 60%, #5e4a45 80%, #3a2e2c 100%);
  }
  .headline-box { position: absolute; left: 415px; top: 194px; width: 217px; height: 197px; background: var(--blush); }

  .brand { position: absolute; left: 91px; top: 48px; display: flex; align-items: center; gap: 8px; }
  .brand-dot { width: 14px; height: 14px; border-radius: 50%; background: var(--green); }
  .brand-name { font-size: 30px; font-weight: 600; color: var(--brown); letter-spacing: -0.5px; line-height: 1; }

  .nav-link { position: absolute; left: 948px; top: 64px; font-size: 20px; font-weight: 500; color: var(--brown); text-decoration: none; }
  .cart { position: absolute; left: 1071px; top: 56px; width: 44px; height: 44px; border-radius: 50%; background: var(--blush); display: flex; align-items: center; justify-content: center; }
  .cart-count { position: absolute; left: 1098px; top: 45px; width: 24px; height: 24px; border-radius: 50%; background: var(--brown); color: var(--white); font-size: 14px; font-weight: 500; display: flex; align-items: center; justify-content: center; }

  .headline { position: absolute; left: 89px; top: 212px; font-weight: 700; font-size: 66px; line-height: 76px; letter-spacing: -1.5px; }
  .headline .green { color: var(--green); display: block; }
  .headline .dark { color: var(--brown); display: block; }

  .btn-shop { position: absolute; left: 92px; top: 402px; width: 144px; height: 55px; border: 2px solid var(--brown); border-radius: 5px; display: flex; align-items: center; justify-content: center; font-size: 22px; font-weight: 500; color: var(--brown); text-decoration: none; }
  .partner-badge { position: absolute; left: 249px; top: 402px; width: 157px; height: 55px; border-radius: 6px; background: var(--ink); }

  .features { position: absolute; left: 0; top: 561px; width: 1200px; height: 114px; }
  .feature { position: absolute; top: 35px; display: flex; gap: 14px; align-items: flex-start; }
  .feature svg { width: 40px; height: 44px; flex: none; }
  .feature h3 { font-size: 22px; font-weight: 700; line-height: 26px; color: var(--brown); }
  .feature p { font-size: 16px; font-weight: 400; line-height: 22px; color: var(--brown); letter-spacing: 0.3px; }
</style>
</head>
<body>
  <section class="hero">
    <div class="hero-photo" role="img" aria-label="Smiling woman sitting on a fluffy rug in a living room, petting a beagle"></div>
    <div class="headline-box"></div>

    <div class="brand">
      <span class="brand-dot"></span>
      <span class="brand-name">PawPatch Grass</span>
    </div>

    <a class="nav-link" href="#">About Us</a>
    <div class="cart">
      <svg width="20" height="20" viewBox="0 0 20 20" fill="none" stroke="#5a1f0e" stroke-width="2">
        <path d="M6 8V6a4 4 0 0 1 8 0v2"/>
        <rect x="3" y="8" width="14" height="10" rx="2"/>
        <path d="M7 12a3 3 0 0 0 6 0"/>
      </svg>
    </div>
    <div class="cart-count">0</div>

    <h1 class="headline">
      <span class="green">100% natural &amp;</span>
      <span class="dark">vet approved</span>
    </h1>

    <a class="btn-shop" href="#">Shop Now</a>
    <div class="partner-badge" role="img" aria-label="Marketplace purchase badge"></div>
  </section>

  <section class="features">
    <div class="feature" style="left:89px;">
      <svg viewBox="0 0 40 44" fill="none" stroke="#5a1f0e" stroke-width="2.5">
        <path d="M20 20V3M13 10l7-7 7 7"/>
        <path d="M3 18h34v6H3zM6 24v18h28V24"/>
        <path d="M20 24v18M10 32l3 3 5-6"/>
      </svg>
      <div><h3>Worldwide Shipping</h3><p>Get gree shipping over $50</p></div>
    </div>
    <div class="feature" style="left:467px;">
      <svg viewBox="0 0 40 44" fill="none" stroke="#5a1f0e" stroke-width="2.5">
        <path d="M20 3l16 6v12c0 10-7 17-16 20C11 38 4 31 4 21V9z"/>
        <circle cx="20" cy="22" r="8"/>
        <path d="M16 22l3 3 5-6"/>
      </svg>
      <div><h3>Secured Payments</h3><p>Accept all major credit cards</p></div>
    </div>
    <div class="feature" style="left:854px;">
      <svg viewBox="0 0 40 44" fill="none" stroke="#5a1f0e" stroke-width="2.5">
        <rect x="3" y="5" width="34" height="34" rx="3"/>
        <path d="M3 12h34"/>
        <path d="M16 25h16l-4-4M28 32H14l4 4"/>
      </svg>
      <div><h3>Free Returns</h3><p>30-days free eturn policy</p></div>
    </div>
  </section>
</body>
</html>
```